Website for a Pittsburgh Musical Production

We are creating a website for a musical stage production. Content and copy is included below. We are targeting production in early 2023.

Coding

Coded - Design and coding required

Number of Pages Required

1 page

```html
<!DOCTYPE html>
<html lang="en">
<head>
<meta charset="utf-8">
<title>Prometheus The Rock Opera</title>
<link href="https://fonts.googleapis.com/css2?family=Exo+2:wght@400;500&family=Jura:wght@400;500;600&display=swap" rel="stylesheet">
<style>
:root{
  --black:#000;
  --panel:#1a1a1a;
  --white:#fff;
  --text:#d8d8d8;
  --green:#7fb66f;
}
*{margin:0;padding:0;box-sizing:border-box}
html,body{width:1200px;height:3350px;overflow:hidden;background:var(--black)}
body{position:relative;font-family:"Jura",sans-serif;color:var(--white)}
section,header,footer{position:absolute;left:0;width:1200px}
.display{font-family:"Exo 2",sans-serif;font-weight:400;letter-spacing:2px;text-align:center}
.btn{position:absolute;display:flex;align-items:center;justify-content:center;border-radius:26px;font-family:"Exo 2",sans-serif;font-size:18px;letter-spacing:.5px;color:var(--white)}

/* header */
.site-header{top:0;height:97px;background:var(--black)}
.brand{position:absolute;left:144px;top:30px;font-family:"Jura",sans-serif;font-weight:600;font-size:30px;color:var(--green)}
.main-nav{position:absolute;left:408px;top:43px;display:flex;gap:23px;font-size:12px;font-weight:500;letter-spacing:.4px}
.main-nav a{color:var(--white);text-decoration:none}
.main-nav a.active{color:var(--green);border-bottom:2px solid var(--green);padding-bottom:10px}

/* hero */
.hero{top:97px;height:575px;background:radial-gradient(ellipse at 30% 30%,#3c4b38 0%,#1e2a26 35%,#101716 70%,#0b1011 100%)}
.hero-art{position:absolute;inset:0}
.hero h1{position:absolute;top:148px;width:100%;font-size:47px;letter-spacing:3px}
.hero .tagline{position:absolute;top:210px;width:100%;text-align:center;font-size:15px;letter-spacing:10px;color:var(--text)}
.btn-trailer{left:515px;top:258px;width:170px;height:50px;background:var(--green);border:2px solid #e8f2e4}
.dots{position:absolute;top:515px;left:580px;display:flex;gap:9px}
.dots span{width:7px;height:7px;border-radius:50%;background:var(--white)}
.dots span.off{background:transparent;border:1px solid var(--white)}

/* welcome */
.welcome{top:672px;height:412px;background:linear-gradient(180deg,#1d2b2d 0%,#263839 50%,#151d1e 100%)}
.welcome h2{position:absolute;top:62px;width:100%;font-size:39px;color:var(--green)}
.welcome .copy{position:absolute;top:122px;left:222px;width:756px;text-align:center;font-size:14px;line-height:22px;letter-spacing:.5px;color:var(--text)}
.welcome .copy p+p{margin-top:15px}
.btn-read{left:516px;top:286px;width:168px;height:52px;border:2px solid #e0e0e0;background:transparent}

/* media */
.media{top:1084px;height:958px;background:linear-gradient(180deg,#111 0%,#060606 100%)}
.media h2{position:absolute;top:52px;width:100%;font-size:35px}
.media .lede{position:absolute;top:106px;width:100%;text-align:center;font-size:14px;letter-spacing:.5px;color:var(--text)}
.gallery{position:absolute;left:144px;top:164px;display:grid;grid-template-columns:repeat(3,288px);grid-auto-rows:296px;column-gap:24px;row-gap:23px}
.gallery div{width:288px;height:296px}
.btn-more{left:513px;top:828px;width:174px;height:52px;background:#1e1e1e}

/* about */
.about{top:2042px;height:615px;background:var(--panel)}
.about h2{position:absolute;top:52px;width:100%;font-size:35px}
.about .story{position:absolute;left:144px;top:172px;width:340px;font-size:16px;line-height:28px;letter-spacing:1.1px;color:var(--text)}
.btn-learn{left:144px;top:464px;width:162px;height:48px;background:var(--green)}
.about-photo{position:absolute;left:524px;top:147px;width:533px;height:393px;border:6px solid #3a3a3a;background:linear-gradient(180deg,#7a85a8 0%,#5c6680 50%,#3f4552 100%)}

/* video */
.video{top:2657px;height:416px;background:linear-gradient(180deg,#1d2b2d 0%,#27393a 50%,#121a1b 100%)}
.video h2{position:absolute;top:86px;width:100%;font-size:35px}
.video .lede{position:absolute;top:145px;left:205px;width:790px;text-align:center;font-size:12px;line-height:15px;letter-spacing:.3px;color:var(--text)}
.play{position:absolute;left:563px;top:199px}

/* footer */
.site-footer{top:3073px;height:277px;background:#060606}
.footer-col{position:absolute;top:44px;font-size:12px;line-height:24px}
.footer-col h3{font-family:"Jura",sans-serif;font-weight:500;font-size:14px;color:var(--green);margin-bottom:6px}
.footer-col a{display:block;color:var(--white);text-decoration:none}
.col-nav-a{left:144px}
.col-nav-b{left:336px;top:74px}
.col-contact{left:560px}
.col-contact .person{letter-spacing:4px}
.col-mail{left:798px;top:76px;line-height:40px}
.col-mail span{display:flex;align-items:center;gap:5px}
.footer-rule{position:absolute;left:144px;top:215px;width:913px;height:1px;background:#222}
.copyright{position:absolute;left:144px;top:238px;font-size:10.5px;color:var(--text)}
.legal{position:absolute;left:900px;top:238px;font-size:9px;color:#555}
</style>
</head>
<body>

<header class="site-header">
  <div class="brand">Prometheus</div>
  <nav class="main-nav">
    <a class="active">HOME</a><a>NEWS</a><a>STORY</a><a>MUSIC</a><a>MEDIA</a><a>COMPOSERS</a><a>PRODUCTIONS</a><a>MERCHANDISE</a><a>CONTACT</a>
  </nav>
</header>

<section class="hero">
  <div class="hero-art" role="img" aria-label="Dark green stage artwork of the creature"></div>
  <h1 class="display">PROMETHEUS THE ROCK OPERA</h1>
  <p class="tagline">We are a new Prometheus The Rock Opera</p>
  <div class="btn btn-trailer">VIEW TRAILER</div>
  <div class="dots"><span class="off"></span><span></span><span></span></div>
</section>

<section class="welcome" role="img" aria-label="Dim teal stage backdrop with silhouetted figures">
  <h2 class="display">WELCOME TO PROMETHEUS</h2>
  <div class="copy">
    <p>Lorem ipsum dolor sit amet, consectetur adipiscing elit, sed do eiusmod tempor incididunt ut labore et dolore magna aliqua. Ut enim ad minim veniam, quis nostrud exercitation ullamco laboris nisi ut aliquip ex ea commodo consequat.</p>
    <p>Neque porro quisquam est, qui dolorem ipsum quia dolor sit amet, consectetur, adipisci velit, sed quia non numquam eius modi tempora incidunt ut labore et dolore magnam aliquam quaerat voluptatem.</p>
  </div>
  <div class="btn btn-read">READ MORE</div>
</section>

<section class="media">
  <h2 class="display">PROMETHEUS MEDIA</h2>
  <p class="lede">Excepteur sint occaecat cupidatat non proident, sunt in culpa qui officia deserunt mollit anim id est laborum</p>
  <div class="gallery">
    <div role="img" aria-label="Production photo of sailors on deck" style="background:linear-gradient(160deg,#3b4466,#2a2e40)"></div>
    <div role="img" aria-label="Production photo of the creature in dim light" style="background:linear-gradient(160deg,#1f2a35,#3a3126)"></div>
    <div role="img" aria-label="Production photo of the scientist under green light" style="background:linear-gradient(160deg,#1c2a22,#355a34)"></div>
    <div role="img" aria-label="Painted artwork of the scientist with lightning" style="background:linear-gradient(160deg,#4a6a90,#6a2a3a)"></div>
    <div role="img" aria-label="Production photo of the creature embracing a figure" style="background:linear-gradient(160deg,#5a6a85,#b0a89a)"></div>
    <div role="img" aria-label="Production photo of the creature raising its hands" style="background:linear-gradient(160deg,#3a4a66,#a89a88)"></div>
  </div>
  <div class="btn btn-more">VIEW MORE</div>
</section>

<section class="about">
  <h2 class="display">ABOUT PROMETHEUS</h2>
  <p class="story">Like Ada Verlaine's classic tale, our story begins on the frigid seas of the Arctic Circle, where mountains of ice block Captain Halvard and his crew on their voyage to the North Pole. Ignoring the imminent mutiny of his sailors, Captain Halvard has locked himself in his cabin and tends to a dying stranger whom he recently dragged aboard.</p>
  <div class="btn btn-learn">LEARN MORE</div>
  <div class="about-photo" role="img" aria-label="Production photo of the ship's crew on an icy stage"></div>
</section>

<section class="video" role="img" aria-label="Dim teal stage backdrop with silhouetted figures">
  <h2 class="display">PROMETHEUS VIDEO</h2>
  <p class="lede">Temporibus autem quibusdam et aut officiis debitis aut rerum necessitatibus saepe eveniet ut et voluptates repudiandae<br>sint et molestiae non recusandae.</p>
  <svg class="play" width="74" height="74" viewBox="0 0 74 74">
    <circle cx="37" cy="37" r="35" fill="#000" stroke="#fff" stroke-width="2.5"/>
    <path d="M28 22 L54 37 L28 52 Z" fill="#fff"/>
  </svg>
</section>

<footer class="site-footer">
  <div class="footer-col col-nav-a">
    <h3>Navigation</h3>
    <a>News</a><a>Story</a><a>Music</a><a>Media</a><a>Composers</a>
  </div>
  <div class="footer-col col-nav-b">
    <a>Productions</a><a>Merchandise</a><a>Contact</a>
  </div>
  <div class="footer-col col-contact">
    <h3>Contact Info</h3>
    <div class="person">Rory Castell</div>
    <div class="person">Media Director</div>
    <div>Prometheus The Rock</div>
    <div>Opera, LLC</div>
  </div>
  <div class="footer-col col-mail">
    <span><svg width="12" height="10" viewBox="0 0 12 10"><rect x=".5" y=".5" width="11" height="9" fill="none" stroke="#7fb66f"/><path d="M.5 .5 L6 5.5 L11.5 .5" fill="none" stroke="#7fb66f"/></svg>info@prometheusrockstage.com</span>
    <span><svg width="12" height="10" viewBox="0 0 12 10"><rect x=".5" y=".5" width="11" height="9" fill="none" stroke="#7fb66f"/><path d="M.5 .5 L6 5.5 L11.5 .5" fill="none" stroke="#7fb66f"/></svg>media@prometheusrockstage.com</span>
  </div>
  <div class="footer-rule"></div>
  <p class="copyright">Copyrights © 2021 Prometheus The Rock Opera. All rights reserved.</p>
  <p class="legal">Terms of Use &nbsp; / &nbsp; Privacy Policy</p>
</footer>

</body>
</html>
```